ROLL UP CREATION

For a trade show we need three visuals to be seen see pdf file with slogans and photos. I expect from you a nice and attractive formatting that is urgent. the files must be in high definition for the printer. You will find enclosed the 3 visuals, photos the basic logo by adding the .com and the photo of the Rollup For a trade show we need to see the pdf file with slogans and photos. I expect from you a nice and attractive formatting that is urgent. the files must be in high definition for the printer. For a trade show we need to see the pdf file with slogans and photos. I expect from you a nice and attractive formatting that is urgent. the files must be in high definition for the printer. For a trade show we need to see the pdf file with slogans and photos. I expect from you a nice and attractive formatting that is urgent. the files must be in high definition for the printer. For a trade show we need to see the pdf file with slogans and photos. I expect from you a nice and attractive formatting that is urgent. the files must be in high definition for the printer. For a trade show we need to see the pdf file with slogans and photos. I expect from you a nice and attractive formatting that is urgent. the files must be in high definition for the printer. For a trade show we need to see the pdf file with slogans and photos. I expect from you a nice and attractive formatting that is urgent. the files must be in high definition for the printer. For a trade show we need to see the pdf file with slogans and photos. I expect from you a nice and attractive formatting that is urgent. the files must be in high definition for the printer. For a trade show we need to see the pdf file with slogans and photos. I expect from you a nice and attractive formatting that is urgent. the files must be in high definition for the printer. For a trade show we need to see the pdf file with slogans and photos. I expect from you a nice and attractive formatting that is urgent. the files must be in high definition for the printer.

Target Market(s)

Professional

Industry/Entity Type

Trade

Requirements
Must have
• the project the messages and the photos are chosen all the way to a nice and professional result. This is urgently the size of the rollup is 200/85.
Nice to have
• the bottom of the rollup on 40 cm must be just color because in an exhibition the visitors can not see the messages near the ground.
Should not have
• no green color

```html
<!DOCTYPE html>
<html lang="fr">
<head>
<meta charset="utf-8">
<title>Roll-up DTG</title>
<link href="https://fonts.googleapis.com/css2?family=Montserrat:wght@500;700&display=swap" rel="stylesheet">
<style>
  :root {
    --stage: #000000;
    --paper: #f1f1f3;
    --brand-blue: #2d5a8e;
    --brand-purple: #8e4f98;
    --white: #ffffff;
    --photo-light: #eeeeee;
    --photo-mid: #b9b4ad;
  }
  html, body {
    margin: 0;
    padding: 0;
    width: 1200px;
    height: 2613px;
    overflow: hidden;
    background: var(--stage);
  }
  .rollup {
    position: absolute;
    left: 78px;
    top: 78px;
    width: 1044px;
    height: 2455px;
    background: var(--paper);
    overflow: hidden;
    font-family: "Montserrat", Arial, sans-serif;
  }
  .rollup__artwork {
    position: absolute;
    inset: 0;
  }
  .brand {
    position: absolute;
    top: 128px;
    left: 0;
    width: 100%;
    display: flex;
    justify-content: center;
    align-items: center;
    gap: 28px;
    color: var(--brand-blue);
    font-weight: 500;
    font-size: 104px;
    letter-spacing: -1px;
    line-height: 1;
  }
  .brand__mark {
    width: 86px;
    height: 86px;
    background: var(--brand-blue);
    border-radius: 50%;
  }
  .headline {
    position: absolute;
    top: 350px;
    left: 0;
    width: 100%;
    margin: 0;
    text-align: center;
    color: var(--brand-blue);
    font-weight: 700;
    font-size: 68px;
    line-height: 114px;
  }
  .tagline {
    position: absolute;
    top: 1910px;
    left: 0;
    width: 100%;
    margin: 0;
    text-align: center;
    color: var(--white);
    font-weight: 700;
    font-size: 68px;
    line-height: 104px;
  }
</style>
</head>
<body>
<main class="rollup">
  <svg class="rollup__artwork" width="1044" height="2455" viewBox="0 0 1044 2455" aria-hidden="false">
    <defs>
      <linearGradient id="photoTone" x1="0" y1="0" x2="0" y2="1">
        <stop offset="0" stop-color="var(--paper)" stop-color-fallback="#f1f1f3" style="stop-color:#f1f1f3"/>
        <stop offset="0.35" stop-color="#d9d6d2"/>
        <stop offset="1" stop-color="#a9a39b"/>
      </linearGradient>
    </defs>
    <rect class="photo" x="0" y="760" width="1044" height="960" fill="url(#photoTone)" role="img" aria-label="Photo de deux copropriétaires étonnés penchés au-dessus d'une table, l'un portant des lunettes rondes, l'autre des lunettes noires"/>
    <path class="wave wave--purple" d="M0,1625 Q620,1600 1044,1450 L1044,2455 L0,2455 Z" fill="#8e4f98"/>
    <path class="wave wave--white" d="M0,1710 Q640,1700 1044,1555 L1044,2455 L0,2455 Z" fill="#ffffff"/>
    <path class="wave wave--blue" d="M0,1780 Q660,1770 1044,1595 L1044,2455 L0,2455 Z" fill="#2d5a8e"/>
  </svg>

  <div class="brand">
    <span class="brand__mark"></span>
    <span class="brand__name">batiscope.com</span>
  </div>

  <h1 class="headline">La réalisation d'un<br>DTG va étonner plus<br>d’un copropriétaire !!</h1>

  <p class="tagline">Le DTG, l'outil qui<br>optimise vos charges et<br>votre patrimoine...</p>
</main>
</body>
</html>
```